Business Card Design Project

I help solve problems that people have with real estate, so I buy homes for cash that they no longer want, can't afford, inherited, etc. and fix and sell them or rent them or take over mortgage payments. See website: www.quickdeedhomestead.com

Industry/Entity Type

Real Estate

Contact Information for Business Card

Not exactly sure. Looking for a design that either is similar to the website www.quickdeedhomestead.com or that reflects what I do as described below. If it can look a little luxurious to show I can buy the houses for cash and I fix them and sell them, it's a bonus. I seem to like some of the higher end things like foil or black or something that makes it stand out.

Font styles to use
Serif

Requirements
Nice to have
• I seem to like black or clear. I like things to stand out and be different.

```html
<!DOCTYPE html>
<html lang="en">
<head>
<meta charset="utf-8">
<title>Keystone Renewal Homes – Business Cards</title>
<link href="https://fonts.googleapis.com/css2?family=Libre+Baskerville:wght@400;700&display=swap" rel="stylesheet">
<style>
  :root {
    --stage: #1b1c1e;
    --card: #262827;
    --card-panel: #2c362b;
    --green: #6fc23d;
    --green-soft: #8bd45a;
    --text: #e8e8e4;
    --muted: #b9bcb6;
  }
  * { box-sizing: border-box; margin: 0; padding: 0; }
  html, body {
    width: 1200px; height: 800px; overflow: hidden;
    background: var(--stage);
    font-family: "Libre Baskerville", "Times New Roman", serif;
    color: var(--text);
  }
  .canvas { position: relative; width: 1200px; height: 800px; }
  .card {
    position: absolute; width: 560px; height: 320px;
    background: var(--card);
    box-shadow: 0 18px 40px rgba(0,0,0,.55);
    overflow: hidden;
  }
  .card--front { left: 80px; top: 70px; }
  .card--back { left: 560px; top: 420px; }

  .card__panel {
    position: absolute;
    background: linear-gradient(160deg, var(--card-panel), #272c27);
  }
  .card--front .card__panel { left: 150px; top: 40px; width: 260px; height: 240px; }
  .card--back .card__panel { right: 0; top: 0; width: 230px; height: 170px; }

  .wordmark {
    color: var(--green);
    font-weight: 700;
    text-transform: uppercase;
    letter-spacing: 1px;
    line-height: 1.15;
  }
  .front__content {
    position: absolute; inset: 0;
    display: flex; flex-direction: column; align-items: center; justify-content: center;
    text-align: center;
  }
  .front__content .wordmark { font-size: 30px; }
  .front__url { margin-top: 18px; font-size: 12px; letter-spacing: 3px; color: var(--text); }

  .back__wordmark { position: absolute; left: 40px; top: 52px; font-size: 28px; }
  .back__rule {
    position: absolute; left: 40px; top: 186px; width: 480px; height: 1px;
    background: var(--green);
  }
  .contact { position: absolute; left: 40px; top: 200px; }
  .contact__name { color: var(--green); font-weight: 700; font-size: 15px; text-transform: uppercase; }
  .contact__role { font-size: 11px; color: var(--text); margin-bottom: 8px; }
  .contact__list { list-style: none; font-size: 11px; }
  .contact__list li { display: flex; align-items: center; gap: 8px; margin-bottom: 4px; }
  .contact__icon { width: 16px; height: 16px; flex: none; }
  .address {
    position: absolute; right: 34px; top: 205px;
    font-size: 11px; line-height: 1.6; text-align: right; color: var(--text);
  }
</style>
</head>
<body>
<main class="canvas">
  <section class="card card--front" aria-label="Card front">
    <div class="card__panel"></div>
    <div class="front__content">
      <div class="wordmark">Keystone Renewal<br>Homes</div>
      <div class="front__url">www.quickdeedhomestead.com</div>
    </div>
  </section>

  <section class="card card--back" aria-label="Card back">
    <div class="card__panel"></div>
    <div class="wordmark back__wordmark">Keystone Renewal<br>Homes</div>
    <div class="back__rule"></div>
    <div class="contact">
      <div class="contact__name">Dana Whitfield</div>
      <div class="contact__role">CEO</div>
      <ul class="contact__list">
        <li>
          <svg class="contact__icon" viewBox="0 0 16 16"><circle cx="8" cy="8" r="7" fill="none" stroke="var(--green)" stroke-width="1.2"/><rect x="5.5" y="4" width="5" height="8" rx="1" fill="none" stroke="var(--green)" stroke-width="1.1"/></svg>
          555 555 5555
        </li>
        <li>
          <svg class="contact__icon" viewBox="0 0 16 16"><circle cx="8" cy="8" r="7" fill="var(--green)"/><rect x="4.3" y="5.3" width="7.4" height="5.4" fill="none" stroke="var(--card)" stroke-width="1"/><path d="M4.3 5.3 8 8.4l3.7-3.1" fill="none" stroke="var(--card)" stroke-width="1"/></svg>
          hello@keystonerenewal.com
        </li>
        <li>
          <svg class="contact__icon" viewBox="0 0 16 16"><circle cx="8" cy="8" r="7" fill="var(--green)"/><circle cx="8" cy="8" r="4" fill="none" stroke="var(--card)" stroke-width="1"/><path d="M4 8h8M8 4c-2 2.5-2 5.5 0 8M8 4c2 2.5 2 5.5 0 8" fill="none" stroke="var(--card)" stroke-width=".9"/></svg>
          www.quickdeedhomestead.com
        </li>
      </ul>
    </div>
    <address class="address" style="font-style:normal">PO BOX 123 your address<br>2nd street Melbourne</address>
  </section>
</main>
</body>
</html>
```